Sell the dream! Property investment proposal document

We are looking for a proposal document which outlines our vision for property development. The purpose of the document is to raise investment from investors - sell the dream!
Brief summary:
Tarrow Dwellings Developments, is an emerging New Zealand property investment company with a focus on providing unique property investment opportunities.
Our expertise and capabilities in architectural modular homes provide us with a remarkable advantage in tackling the development of properties that are typically considered challenging, remote, or uniquely positioned.
Our specialization in this niche sector of property development not only sets us apart from competitors, but also paves the way for lucrative investment opportunities in the New Zealand property market.
Feel free to use any images from www.tarrowdwellings.co.nz
Target Market(s)
investors for a unique property development opportunity
Industry/Entity Type
luxury property development in unique locations throughout New Zealand
Font styles to use
Colors
Designer to choose only greyscale colors for use in the design.
Look and feel

```html
<!DOCTYPE html>
<html lang="en">
<head>
<meta charset="utf-8">
<title>Tarrow Dwellings – Investment Proposal</title>
<link rel="stylesheet" href="https://fonts.googleapis.com/css2?family=Lato:wght@300;400;700&display=swap">
<style>
  :root {
    --stage: #a3a3a3;
    --ink: #0a0a0a;
    --paper: #f1f1f1;
    --white: #ffffff;
    --text-dark: #1e1e1e;
    --text-light: #d8d8d8;
    --accent: #b08a62;
    --muted: #9a9a9a;
  }
  * { box-sizing: border-box; margin: 0; padding: 0; }
  html, body { width: 1004px; height: 1200px; overflow: hidden; }
  body {
    background: var(--stage);
    font-family: 'Lato', sans-serif;
    position: relative;
  }
  .spread {
    position: absolute;
    left: 42px;
    width: 920px;
    height: 326px;
    display: flex;
    box-shadow: 0 6px 18px rgba(0,0,0,0.25);
  }
  .spread--cover { top: 30px; }
  .spread--overview { top: 434px; }
  .spread--advantage { top: 838px; }
  .page { position: relative; width: 460px; height: 100%; overflow: hidden; }
  .page--dark { background: var(--ink); color: var(--text-light); }
  .page--light { background: var(--paper); color: var(--text-dark); }
  .photo { position: absolute; }

  /* Cover spread */
  .back-brand {
    position: absolute; left: 150px; top: 146px;
    font-size: 24px; font-weight: 300; color: var(--white); letter-spacing: 1px;
  }
  .back-contact {
    position: absolute; left: 238px; top: 146px;
    font-size: 6.2px; line-height: 1.45; color: var(--text-light);
  }
  .back-contact .web { color: var(--white); font-weight: 700; margin-top: 2px; }
  .back-contact .social { margin-top: 3px; display: flex; gap: 8px; align-items: center; }
  .dot { display: inline-block; width: 4px; height: 4px; border-radius: 50%; background: var(--text-light); margin-right: 2px; vertical-align: middle; }
  .cover-tagline {
    position: absolute; left: 10px; top: 238px;
    font-size: 7.5px; line-height: 1.35; color: var(--white);
  }
  .cover-brand {
    position: absolute; right: 12px; top: 232px;
    font-size: 26px; font-weight: 400; color: var(--white);
  }

  /* Section headings */
  .section-title {
    position: absolute;
    font-size: 7.5px; letter-spacing: 2.6px; text-transform: uppercase;
    color: var(--accent); font-weight: 400;
    padding: 5px 10px;
    border: 0.8px solid var(--accent);
  }
  .page--dark .section-title { color: var(--text-light); border-color: var(--muted); }
  .body-copy {
    position: absolute;
    font-size: 5.6px; line-height: 1.5;
  }
  .body-copy p + p { margin-top: 4px; }
  .body-copy strong { font-weight: 700; }
  .page--dark .body-copy { color: #bdbdbd; }
  .page--dark .body-copy.warm { color: #c9a37a; }
</style>
</head>
<body>

<!-- Cover spread -->
<section class="spread spread--cover">
  <div class="page page--dark back-cover">
    <div class="back-brand">Tarrow</div>
    <div class="back-contact">
      <div>Ravensdale, Auckland</div>
      <div>sales@tarrowdwellings.co.nz</div>
      <div>09 555 0142</div>
      <div class="web">www.tarrowdwellings.co.nz</div>
      <div class="social"><span><span class="dot"></span>@tarrow_dwellings</span><span><span class="dot"></span>/TarrowDwellingsNZ</span></div>
    </div>
  </div>
  <div class="page page--dark front-cover">
    <div class="photo" role="img" aria-label="Bedroom with floor-to-ceiling window over the sea" style="left:0;top:30px;width:85px;height:199px;background:linear-gradient(180deg,#cfcfcf 0%,#b9b6b0 50%,#e2dfd9 80%,#8e8a84 100%);"></div>
    <div class="photo" role="img" aria-label="Living room with round coffee table opening to a coastal headland at dusk" style="left:111px;top:30px;width:235px;height:199px;background:linear-gradient(90deg,#bdb8b0 0%,#8a8478 35%,#6e6652 55%,#57503a 100%);"></div>
    <div class="photo" role="img" aria-label="Glazed hallway looking out to grass" style="left:374px;top:30px;width:86px;height:199px;background:linear-gradient(180deg,#dcdcdc 0%,#9a9a92 40%,#5f5f58 75%,#bdbdb8 100%);"></div>
    <div class="cover-tagline">Modular<br>Architectural<br>Homes</div>
    <div class="cover-brand">Tarrow</div>
  </div>
</section>

<!-- Business overview spread -->
<section class="spread spread--overview">
  <div class="page page--dark">
    <div class="section-title" style="left:18px;top:26px;">Business Overview</div>
    <div class="photo" role="img" aria-label="Single-storey modular home on a lawn among trees" style="left:235px;top:44px;width:225px;height:140px;background:linear-gradient(180deg,#d6dde2 0%,#b3bcc0 35%,#4d4d48 60%,#6f8a3e 80%,#55702e 100%);"></div>
    <div class="body-copy" style="left:40px;top:112px;width:170px;">
      <p><strong>Tarrow Dwellings Developments</strong> is an emerging New Zealand property investment company with a focus on providing unique property investment opportunities. Our expertise and capabilities in architectural modular homes provide us with a remarkable advantage in tackling the development of properties that are typically considered challenging, remote, or uniquely positioned.</p>
      <p>As a company with 48 employees boasting a wealth of experience in managing complex architectural projects, we understand the intricacies of such ventures. This allows us to not only execute projects efficiently but also to deliver exceptional results within condensed time frames.</p>
      <p>By capitalising on our ability to develop difficult, remote, or one-of-a-kind properties swiftly and effectively, Tarrow Dwellings Developments offers investors a rare chance to engage in projects that promise exceptional profitability in the New Zealand property market.</p>
      <p>Our specialization in this niche sector of property development not only sets us apart from competitors, but also paves the way for lucrative investment opportunities in the New Zealand property market.</p>
    </div>
  </div>
  <div class="page page--light">
    <div class="photo" role="img" aria-label="Timber-clad home with carport under gum trees" style="left:0;top:14px;width:160px;height:150px;background:linear-gradient(180deg,#e6ecef 0%,#9aa7a0 45%,#6d5d4d 70%,#c9c9c6 100%);"></div>
    <div class="photo" role="img" aria-label="Dark home on a grassy rise above the coast" style="left:160px;top:14px;width:150px;height:150px;background:linear-gradient(180deg,#9fb2c6 0%,#7f8c8c 45%,#4d4e48 62%,#7c9a45 100%);"></div>
    <div class="photo" role="img" aria-label="Interior lounge chair beside glazing over a cliff" style="left:310px;top:14px;width:150px;height:150px;background:linear-gradient(180deg,#4a443e 0%,#8d8a7f 45%,#6c6a5d 70%,#2f2c29 100%);"></div>
    <div class="section-title" style="left:24px;top:180px;">Business Origins</div>
    <div class="body-copy" style="left:24px;top:206px;width:200px;">
      <p><strong>Tarrow Dwellings Developments</strong> was established with the goal of transforming the property investment market in New Zealand by introducing an innovative approach that centers on architectural modular designs and streamlined project timelines. Driven by our enthusiasm for architecture and real estate, we have expanded our successful business model to not only offer financial opportunities for investors but also to expand on our passion for high-end architectural design. With a wealth of experience accumulated over the past six years in the construction and the property market, we are pivoting to focus solely on our property development initiatives, presenting completed Tarrow projects to the market, in exclusive locations.</p>
    </div>
    <div class="body-copy" style="left:244px;top:206px;width:196px;">
      <p>These projects will boast high-quality standards, meticulous attention to detail and landscaping and creative design elements. By introducing completed Tarrow properties into the market, we aim to reach a wider audience, catering to individuals who prefer ready-to-occupy homes over engaging in the design and construction process. This approach also simplifies the financing process for prospective buyers, as established properties are often preferred by financial lenders.</p>
    </div>
  </div>
</section>

<!-- Competitive advantage / financial summary spread -->
<section class="spread spread--advantage">
  <div class="page page--light">
    <div class="section-title" style="left:14px;top:40px;">Competitive Advantage</div>
    <div class="body-copy" style="left:22px;top:70px;width:190px;">
      <p>Our competitive advantage lies in the uniqueness of our property investment opportunities.</p>
      <p>Unlike traditional real estate companies, we focus on offering properties that are not only profitable but also aesthetically pleasing and unique. By catering to the tastes of architecture lovers, we set ourselves apart from the competition and attract a niche market of customers who appreciate the artistry and design of our projects.</p>
      <p>Additionally, the streamlined and condensed timelines facilitated by our modular approach provide quicker returns on investment.</p>
    </div>
    <div class="photo" role="img" aria-label="Living room with fireplace, sofas and nested round tables" style="left:226px;top:0;width:234px;height:326px;background:linear-gradient(180deg,#b9aaa0 0%,#6b5d55 30%,#2b2420 50%,#8a7d72 72%,#d8d0c6 100%);"></div>
  </div>
  <div class="page page--dark">
    <div class="photo" role="img" aria-label="Aerial view of a modular home on a coastal hillside at dusk" style="left:30px;top:18px;width:410px;height:196px;background:linear-gradient(180deg,#8a857a 0%,#6e6a5e 30%,#3e3a2c 55%,#5a4a2e 80%,#3a2f20 100%);"></div>
    <div class="body-copy warm" style="left:22px;top:232px;width:205px;">
      <p>In terms of financial projections, with each development, we anticipate a profit of 10%–20% which will be project dependent. This growth is fueled by the increasing demand for unique property investments in New Zealand and our ability to deliver high-quality services to the market in a condensed time frame. With a solid business model and a dedicated team, we are confident in our ability to achieve success and establish Tarrow Dwellings Investments as a trusted name in the industry.</p>
    </div>
    <div class="section-title" style="left:252px;top:226px;">Financial Summary</div>
    <div class="body-copy warm" style="left:248px;top:254px;width:195px;">
      <p>New Zealand's property market has been experiencing steady growth over the years, making it an attractive destination for property investors. With its beautiful landscapes and strong economy, New Zealand offers a diverse range of investment opportunities for both local and international investors. The demand for quality properties in prime locations continues to rise, creating a favourable environment for property investment companies like ours that can lean on our modular benefits of being able to reach unique and remote locations.</p>
    </div>
  </div>
</section>

</body>
</html>
```